Puslishing House Needs poster Design for Medical Book

We need an advertisement desing for a medical book on cardiology named "Lumivarte" (Hypertension), which 2nd Edition we launched last August. What makes this book special is that this is the first time in history that a hypertension book has a second edition in Brazil and was written by the Vessel Studies Unit of the Austral Guild of Circulatory Medicine in comemoration in its 100 years. The two news about this book is that we sold 1000 units since we launched (which is good) and we have now an ebook version for all tablet, smartphones and readers. From this month on it is going to happen importants hypertension meetings and we want to promote this two news about this book - 1000 units sold and ebook version. We would like to see designs that use orange (the publishing house color) and communicate celebration.

Target Market(s)

Doctors Specialist from several segments like Cardiology, Endocrinology, Nephrology, Nutrition. Most of the target are man with 50 years-old.

Industry/Entity Type

Medical

Requirements
Must have
• The adverstisement must have the attached book cover and publishing house logo (Quorvane) using only the name (without the tree) or the complete logo.
Should not have
• The design should not use old-style, serif fonts like Times new Roman.

```html
<!DOCTYPE html>
<html lang="en">
<head>
<meta charset="utf-8">
<title>Lumivarte – 2nd edition poster</title>
<link rel="stylesheet" href="https://fonts.googleapis.com/css2?family=Open+Sans:ital,wght@0,600;0,700;0,800;1,800&family=Oswald:wght@700&display=swap">
<style>
  :root {
    --green-deep: #0a4626;
    --green-mid: #1d5a2a;
    --olive: #5d5322;
    --orange: #c9431c;
    --orange-deep: #c2361a;
    --title-red: #d8381d;
    --white: #ffffff;
    --ink: #1f2a22;
    --cover-green: #2f6a52;
    --device: #121314;
  }
  * { box-sizing: border-box; margin: 0; padding: 0; }
  html, body { width: 863px; height: 1200px; overflow: hidden; }
  body { font-family: "Open Sans", Arial, sans-serif; color: var(--white); }
  .poster {
    position: relative; width: 863px; height: 1200px; overflow: hidden;
    background: linear-gradient(180deg, var(--green-deep) 0%, var(--green-mid) 30%, var(--olive) 48%, var(--orange) 68%, var(--orange-deep) 100%);
  }
  .tagline {
    position: absolute; top: 112px; left: 0; width: 100%;
    text-align: center; font-style: italic; font-weight: 800;
    font-size: 31px; line-height: 38px;
  }
  .title {
    position: absolute; top: 190px; left: 0; width: 100%; text-align: center;
    font-family: "Oswald", "Arial Narrow", sans-serif; font-weight: 700;
    font-size: 128px; line-height: 140px; color: var(--title-red);
    letter-spacing: 1px; text-shadow: 0 2px 4px rgba(0,0,0,.25);
  }
  .sales {
    position: absolute; top: 378px; left: 0; width: 100%; text-align: center;
    font-weight: 700; font-size: 56px; line-height: 62px;
  }
  .ebook {
    position: absolute; top: 592px; left: 500px; width: 330px; text-align: center;
  }
  .ebook-head { font-weight: 700; font-size: 60px; line-height: 52px; }
  .ebook-note { font-weight: 700; font-size: 15px; line-height: 18px; margin-top: 10px; }

  .book-stack { position: absolute; left: 39px; top: 800px; width: 460px; height: 230px; }
  .book-front {
    position: absolute; left: 118px; top: 504px; width: 254px; height: 432px;
    background: linear-gradient(160deg, #e8eee9 0%, #ffffff 40%, #dfe6e1 100%);
    box-shadow: 8px 10px 18px rgba(0,0,0,.45);
  }
  .cover-art {
    position: absolute; left: 0; top: 0; width: 100%; height: 100%;
    background: linear-gradient(170deg, var(--cover-green) 0%, #6f9a84 30%, #f2f4f2 60%, #cfd6d2 100%);
  }
  .cover-authors {
    position: absolute; top: 26px; left: 118px; color: var(--white);
    font-weight: 700; font-size: 14px; line-height: 19px;
  }
  .cover-title {
    position: absolute; top: 140px; left: 0; width: 100%; text-align: center;
    font-family: "Oswald", sans-serif; font-weight: 700; font-size: 44px; color: var(--title-red);
  }
  .cover-edition {
    position: absolute; bottom: 18px; left: 14px; color: var(--ink);
    font-weight: 600; font-size: 10px;
  }
  .tablet {
    position: absolute; left: 621px; top: 780px; width: 152px; height: 250px;
    background: var(--device); border-radius: 14px; padding: 22px 10px;
    box-shadow: 0 6px 14px rgba(0,0,0,.35);
  }
  .tablet-screen {
    position: relative; width: 100%; height: 100%; overflow: hidden;
    background: linear-gradient(170deg, var(--cover-green) 0%, #7ea390 32%, #f2f4f2 62%, #cfd6d2 100%);
  }
  .tablet-authors { position: absolute; top: 10px; left: 62px; font-size: 7px; font-weight: 700; line-height: 9px; }
  .tablet-title {
    position: absolute; top: 68px; width: 100%; text-align: center;
    font-family: "Oswald", sans-serif; font-weight: 700; font-size: 20px; color: var(--title-red);
  }

  .footer { position: absolute; left: 0; top: 1060px; width: 100%; height: 110px; }
  .seal { position: absolute; left: 33px; top: 16px; width: 60px; height: 60px; border-radius: 50%; background: #2a4f8a; border: 3px solid var(--white); }
  .society {
    position: absolute; left: 108px; top: 26px; width: 260px;
    font-weight: 700; font-size: 12px; line-height: 15px; color: var(--white);
  }
  .url { position: absolute; left: 410px; top: 40px; font-weight: 600; font-size: 15px; }
  .publisher {
    position: absolute; left: 690px; top: 0; width: 130px; height: 106px;
    border: 2px solid var(--title-red); display: flex; flex-direction: column;
    align-items: center; justify-content: flex-end; padding-bottom: 10px;
  }
  .publisher-mark { width: 40px; height: 40px; background: var(--title-red); margin-bottom: 12px; }
  .publisher-name { font-weight: 700; font-size: 16px; color: var(--white); letter-spacing: .5px; }
</style>
</head>
<body>
<main class="poster">
  <p class="tagline">first time in history that a hypertension<br>book has a second edition in Brazil</p>
  <h1 class="title">LUMIVARTE</h1>
  <p class="sales">1000 units sold<br>since launched</p>

  <section class="ebook">
    <h2 class="ebook-head">ebook<br>version</h2>
    <p class="ebook-note">now an ebook version is available for<br>all tablet, smartphones and readers</p>
  </section>

  <svg class="book-stack" viewBox="0 0 460 230" role="img" aria-label="Second copy of the Lumivarte book lying flat beneath the standing copy">
    <polygon points="10,70 300,20 455,120 160,200" fill="#e9eeea"/>
    <polygon points="10,70 160,200 160,225 10,95" fill="#2f6a52"/>
    <polygon points="160,200 455,120 455,140 160,225" fill="#f4f4f2"/>
    <polygon points="10,70 300,20 455,120 160,200" fill="url(#flatCover)" opacity=".7"/>
    <defs>
      <linearGradient id="flatCover" x1="0" y1="0" x2="1" y2="1">
        <stop offset="0" stop-color="#2f6a52"/><stop offset=".6" stop-color="#ffffff"/><stop offset="1" stop-color="#cfd6d2"/>
      </linearGradient>
    </defs>
  </svg>

  <article class="book-front">
    <div class="cover-art" role="img" aria-label="Book cover artwork: green swirl and a blood pressure gauge"></div>
    <p class="cover-authors">Marina T. Coelho<br>Renato Vilar<br>Lucas Abreu</p>
    <p class="cover-title">LUMIVARTE</p>
    <p class="cover-edition">2ª EDIÇÃO</p>
  </article>

  <div class="tablet">
    <div class="tablet-screen" role="img" aria-label="Lumivarte ebook cover on a tablet screen">
      <p class="tablet-authors">Marina T. Coelho<br>Renato Vilar<br>Lucas Abreu</p>
      <p class="tablet-title">LUMIVARTE</p>
    </div>
  </div>

  <footer class="footer">
    <div class="seal" role="img" aria-label="Partner seal"></div>
    <p class="society">Vessel Studies Unit of the Austral Guild of Circulatory Medicine</p>
    <p class="url">www.quorvane.com.br</p>
    <div class="publisher">
      <span class="publisher-mark"></span>
      <span class="publisher-name">QUORVANE</span>
    </div>
  </footer>
</main>
</body>
</html>
```